Bright Ledger Path's Mortgage Arc

For BrightLedgerPath.org - Creating a sequence of web pages for consumers to understand their mortgage through Mortgage Arc. There are six pages - want the designer to be willing to design and code those six pages. Most of the pages are very similar.

```html
<!DOCTYPE html>
<html lang="en">
<head>
<meta charset="utf-8">
<title>Bright Ledger Path – Your Mortgage Profile</title>
<link href="https://fonts.googleapis.com/css2?family=Poppins:wght@400;500;600;700;800&display=swap" rel="stylesheet">
<style>
  :root {
    --header-bg: #f8f8f8;
    --brand-green: #05cb80;
    --brand-blue: #2a5bd7;
    --card-bg: #ffffff;
    --text-dark: #2b2b2b;
    --cell-border: #dedede;
    --cell-highlight: #fffbdd;
    --rule-light: rgba(255,255,255,0.85);
  }
  * { box-sizing: border-box; margin: 0; padding: 0; }
  html, body {
    width: 1200px; height: 927px; overflow: hidden;
    font-family: 'Poppins', sans-serif;
    background: var(--brand-green);
  }
  .page { position: relative; width: 1200px; height: 927px; }

  .site-header {
    position: absolute; left: 0; top: 0; width: 1200px; height: 99px;
    background: var(--header-bg);
  }
  .brand {
    position: absolute; left: 89px; top: 38px;
    display: flex; align-items: center; gap: 9px;
    font-family: 'Poppins', sans-serif;
    font-weight: 500; font-size: 17px; color: var(--brand-blue);
  }
  .brand-mark { width: 30px; height: 30px; background: var(--brand-blue); border-radius: 3px; }

  .profile-title {
    position: absolute; left: 83px; top: 183px;
    font-size: 26px; font-weight: 700; color: #fff; letter-spacing: 0.2px;
  }
  .title-rule {
    position: absolute; left: 83px; top: 230px; width: 1034px; height: 1px;
    background: var(--rule-light);
  }

  .card {
    position: absolute; background: var(--card-bg); border-radius: 13px;
  }
  .card-personal { left: 83px; top: 263px; width: 509px; height: 282px; }
  .card-mortgage { left: 608px; top: 263px; width: 509px; height: 282px; }
  .card-property { left: 83px; top: 564px; width: 1034px; height: 281px; }

  .card-heading {
    position: absolute; left: 18px; top: 17px; right: 18px;
    font-size: 16px; font-weight: 700; color: var(--brand-blue);
    padding-bottom: 4px; border-bottom: 1px solid var(--brand-blue);
    line-height: 20px;
  }

  .info-table {
    position: absolute; border-collapse: collapse; width: 475px;
  }
  .card-personal .info-table, .card-mortgage .info-table { left: 16px; top: 62px; }
  .card-property .table-left { left: 16px; top: 61px; }
  .card-property .table-right { left: 540px; top: 61px; }

  .info-table td {
    height: 32px; border: 1px solid var(--cell-border);
    font-size: 14px; line-height: 1;
  }
  .info-table .label { width: 324px; padding-left: 7px; color: var(--text-dark); font-weight: 400; }
  .info-table .value { width: 151px; text-align: center; color: var(--brand-blue); font-weight: 700; }
  .info-table .value.is-highlight { background: var(--cell-highlight); }

  .action-button {
    position: absolute; left: 16px; top: 236px; width: 475px; height: 29px;
    background: var(--brand-blue); border: none; border-radius: 8px;
    color: #fff; font-family: 'Poppins', sans-serif; font-size: 12.5px; font-weight: 400;
  }
</style>
</head>
<body>
<div class="page">
  <header class="site-header">
    <div class="brand"><span class="brand-mark"></span>Bright Ledger Path</div>
  </header>

  <h1 class="profile-title">YOUR MORTGAGE PROFILE</h1>
  <div class="title-rule"></div>

  <section class="card card-personal">
    <h2 class="card-heading">PERSONAL INFORMATION</h2>
    <table class="info-table">
      <tr><td class="label">Monthly Gross Income</td><td class="value">10,000</td></tr>
      <tr><td class="label">Pay off any Debt?</td><td class="value is-highlight">No-400</td></tr>
      <tr><td class="label">Previous Homeowner (3Yrs)</td><td class="value is-highlight">No</td></tr>
      <tr><td class="label">Number in Household</td><td class="value is-highlight">4</td></tr>
      <tr><td class="label">Coborrower/Spouse on Loan</td><td class="value is-highlight">No</td></tr>
    </table>
    <button class="action-button">Purchase</button>
  </section>

  <section class="card card-mortgage">
    <h2 class="card-heading">MORTGAGE INFORMATION</h2>
    <table class="info-table">
      <tr><td class="label">Loan Purpose</td><td class="value is-highlight">Purchsae</td></tr>
      <tr><td class="label">Term</td><td class="value is-highlight">30 Yrs.</td></tr>
      <tr><td class="label">Type of Interest Rate</td><td class="value is-highlight">Fixed</td></tr>
      <tr><td class="label">Annual Property Taxes</td><td class="value">$2,000</td></tr>
      <tr><td class="label">Annual Home Insurance</td><td class="value">$600</td></tr>
    </table>
    <button class="action-button">Review Questions</button>
  </section>

  <section class="card card-property">
    <h2 class="card-heading">PROPERTY INFORMATION</h2>
    <table class="info-table table-left">
      <tr><td class="label">Own other Property/Rents</td><td class="value">No-$0</td></tr>
      <tr><td class="label">Occupancy</td><td class="value is-highlight">Live in It</td></tr>
      <tr><td class="label">Type of Home</td><td class="value is-highlight">SFR</td></tr>
      <tr><td class="label">Property Location</td><td class="value is-highlight">Utah</td></tr>
      <tr><td class="label">State</td><td class="value is-highlight">Salt Lake</td></tr>
      <tr><td class="label">Country</td><td class="value is-highlight">USA</td></tr>
    </table>
    <table class="info-table table-right">
      <tr><td class="label">Number of Units</td><td class="value is-highlight">1</td></tr>
      <tr><td class="label">Total Monthly Rents (2-4 Units)</td><td class="value is-highlight">NA</td></tr>
      <tr><td class="label">2nd Mortgage</td><td class="value is-highlight">NA</td></tr>
      <tr><td class="label">Term</td><td class="value">NA</td></tr>
      <tr><td class="label">Balance</td><td class="value">NA</td></tr>
      <tr><td class="label">Interest Rate</td><td class="value">NA</td></tr>
    </table>
  </section>
</div>
</body>
</html>
```